Medical Cannabis company is looking for a LOGO design *

SILVER MERIDIAN (SM) is a new company in the Israeli medical cannabis industry. We will engage in PREMIUM medical cannabis growing and cultivation and also manufacturing of HIGH-END cannabis based medical products.
the design should reflect luxury, high-end and Pharma-grade products.
the design should use color GOLD and NOT using the famous cannabis leaf !

Target Market(s)

international medical cannabis Pharmaceutical companies
and of course local and international patients

Contact Information for Business Card

Ron Ben-Amit
Founder and CEO

Silver Meridian
Medical grade cannabis

ronbenamit@mailpost-example.com
972-52-3186407

Colors
ffc214
fbed22

Requirements
Must have
• clean and simple
• luxury
• gold !!
• (can also have green for Cannabis and/or blue for Pharma)
Should not have
• cannabis leaf

```html
<!DOCTYPE html>
<html lang="en">
<head>
<meta charset="utf-8">
<title>Silver Meridian – Business Card</title>
<link rel="stylesheet" href="https://fonts.googleapis.com/css2?family=Nunito:wght@800&family=Open+Sans:wght@400;700&family=Heebo:wght@300;400&display=swap">
<style>
  :root {
    --page-bg: #d9d9d9;
    --card-white: #ffffff;
    --card-dark: #2c2d2e;
    --brand-green: #1fae3c;
    --ink: #1a1a1a;
    --ink-soft: #3a3a3a;
    --gold: #ffc214;
    --gold-light: #fbed22;
  }
  * { margin: 0; padding: 0; box-sizing: border-box; }
  html, body { width: 1200px; height: 900px; overflow: hidden; }
  body {
    background: var(--page-bg);
    font-family: "Open Sans", sans-serif;
    position: relative;
  }
  .card {
    position: absolute;
    left: 285px;
    width: 630px;
    height: 360px;
    overflow: hidden;
    box-shadow: 0 6px 18px rgba(0,0,0,0.18);
  }
  .card-front { top: 70px; background: var(--card-white); }
  .card-back { top: 470px; background: var(--card-dark); }

  /* front */
  .brand {
    position: absolute;
    right: 40px;
    top: 36px;
    text-align: right;
    color: var(--brand-green);
  }
  .brand-name {
    font-family: "Nunito", sans-serif;
    font-weight: 800;
    font-size: 27px;
    line-height: 1;
    letter-spacing: 0.2px;
  }
  .brand-tagline {
    font-family: "Open Sans", sans-serif;
    font-size: 8.5px;
    letter-spacing: 3.2px;
    margin-top: 5px;
  }
  .person {
    position: absolute;
    left: 34px;
    top: 168px;
  }
  .person-name {
    font-weight: 700;
    font-size: 13px;
    letter-spacing: 4.5px;
    color: var(--ink);
  }
  .person-role {
    font-size: 11px;
    letter-spacing: 3.5px;
    color: var(--ink-soft);
    margin-top: 3px;
  }
  .contacts {
    position: absolute;
    left: 34px;
    top: 240px;
    list-style: none;
  }
  .contact {
    display: flex;
    align-items: center;
    gap: 12px;
    font-size: 10.5px;
    font-weight: 700;
    letter-spacing: 3.2px;
    color: var(--ink);
    text-transform: uppercase;
    height: 21px;
  }
  .contact svg { width: 12px; height: 12px; flex: none; fill: var(--ink); }

  /* back */
  .hebrew-mark {
    position: absolute;
    right: 360px;
    top: 152px;
    text-align: right;
    direction: rtl;
    color: var(--gold);
    font-family: "Heebo", sans-serif;
  }
  .hebrew-name {
    font-weight: 400;
    font-size: 31px;
    line-height: 1.05;
  }
  .hebrew-tagline {
    font-weight: 300;
    font-size: 12px;
    letter-spacing: 3px;
    margin-top: 2px;
  }
  .gold-band {
    position: absolute;
    left: 270px;
    right: 0;
    top: 205px;
    height: 66px;
    background: linear-gradient(90deg, var(--gold), var(--gold-light));
  }
</style>
</head>
<body>
  <section class="card card-front" aria-label="Business card front">
    <div class="brand">
      <div class="brand-name">Silver Meridian</div>
      <div class="brand-tagline">MEDICAL GRADE CANNABIS</div>
    </div>
    <div class="person">
      <div class="person-name">RON BEN-AMIT</div>
      <div class="person-role">FOUNDER AND CEO</div>
    </div>
    <ul class="contacts">
      <li class="contact">
        <svg viewBox="0 0 12 12" aria-hidden="true"><path d="M0 2h12v8H0z M1 3l5 3.5L11 3" fill="none" stroke="#1a1a1a" stroke-width="1.2"/></svg>
        ronbenamit@mailpost-example.com
      </li>
      <li class="contact">
        <svg viewBox="0 0 12 12" aria-hidden="true"><circle cx="6" cy="6" r="5" fill="none" stroke="#1a1a1a" stroke-width="1.2"/><path d="M1 6h10M6 1c-2.5 3-2.5 7 0 10M6 1c2.5 3 2.5 7 0 10" fill="none" stroke="#1a1a1a" stroke-width="1"/></svg>
        www.silvermeridian-example.com
      </li>
      <li class="contact">
        <svg viewBox="0 0 12 12" aria-hidden="true"><path d="M2.2 0.8l2 2.4-1.2 1.3c.7 1.6 2 2.9 3.5 3.6l1.3-1.2 2.4 2-1.3 2C5 10.5 1.5 7 .8 2.1z"/></svg>
        972-52-3186407
      </li>
      <li class="contact">
        <svg viewBox="0 0 12 12" aria-hidden="true"><path d="M6 0.5a4 4 0 0 1 4 4c0 3-4 7-4 7s-4-4-4-7a4 4 0 0 1 4-4z M6 3a1.5 1.5 0 1 0 0 3a1.5 1.5 0 1 0 0-3z" fill-rule="evenodd"/></svg>
        24 Orchard Lane Modiin | Israel
      </li>
    </ul>
  </section>

  <section class="card card-back" aria-label="Business card back">
    <div class="hebrew-mark" lang="he">
      <div class="hebrew-name">מרידיאן הכסף</div>
      <div class="hebrew-tagline">קנאביס רפואי</div>
    </div>
    <div class="gold-band"></div>
  </section>
</body>
</html>
```